Landingpages Telefoninterview und Webinar für Technologie-Beratungsunternehmen
Zielgruppe
Unser Unternehmen ist ein IT-Beratungshaus, das sich auf die individuelle Software-Entwicklung im Nexa- und Salesforce-Umfeld spezialisiert hat.
Aufgabenstellung
Um unsere Dienstleistung (Nexa-Beratung) effizienter zu verkaufen, bieten wir unseren Kunden unter anderem 30 Minuten kostenlose Telefonberatung, sowie Webinare an. Für die Anmeldung zu diesen wird jeweils eine Landingpage benötigt. Mit den Landingpages wird das Ziel verfolgt, dass möglichst viele Besucher das kostenlose Telefonat in Anspruch nehmen, bzw. dass es möglichst viele Webinar-Anmeldungen gibt. Die aktuell verwendeten Designs sind nicht zufriedenstellend (siehe angehängte Links), weshalb wir nach Alternativen suchen. Dabei gelten folgende Eckpunkte:
Auf den Landingpages soll jeweils ein Formular eingebaut sein, mittels dessen durch Eingabe und Abschicken der Felder E-Mail, Telefonnummer, Vorname, Nachname und Firma eine Terminanfrage (für die Telefonberatung) bzw. eine Anmeldung (für das Webinar) gemacht wird. Das Formular soll jeweils direkt in die Landinpage integriert sein und nicht über ein Popup funktionieren.
Da die Landingpages Bestandteil einer bestehenden Website werden sollen, ist es wichtig, dass das neue Design zum Stil der Website des Fachbereichs passt (siehe Homepage-Link im Anhang). Dabei soll allerdings nicht einfach das Top-Level Menü der bestehenden Seite übernommen werden. Eine weitere Voraussetzung ist, dass die Landingpages jeweils das Bild unseres Fachbereichsleiters, in diesem speziellen Fall, zeigen.
Im Anhang befinden sich Bilder vom Fachbereichsleite, sowie verwendete Schriften. Als Inspiration unseres Stils kann die ebenfalls angehängte aktuelle Imagebroschüre dienen.
Wir freuen uns auf kreative und innovative Designs.

```html
<!DOCTYPE html>
<html lang="de">
<head>
<meta charset="utf-8">
<title>Kostenlose Telefonberatung – Kernfeld</title>
<link href="https://fonts.googleapis.com/css2?family=Jost:wght@400;500;700&display=swap" rel="stylesheet">
<style>
:root{
  --white:#ffffff;
  --sand:#c4a077;
  --sand-dark:#a6815a;
  --orange:#e8570c;
  --ink:#2b2b2b;
  --muted:#8a8a8a;
  --paper:#f1f1f0;
  --footer:#e8e7e5;
  --field-text:#6b6b6b;
}
*{box-sizing:border-box;margin:0;padding:0}
html,body{width:1200px;height:920px;overflow:hidden}
body{font-family:"Jost",sans-serif;color:var(--ink);background:var(--white);position:relative}
.site-header{height:160px;position:relative}
.brand{position:absolute;left:110px;top:50px;font-size:34px;font-weight:700;color:#4a4a4a;letter-spacing:.5px}
.hero{position:absolute;left:0;top:160px;width:1200px;height:426px;background:var(--paper)}
.form-card{position:absolute;left:110px;top:73px;width:498px;height:281px;background:var(--sand);box-shadow:0 6px 10px rgba(0,0,0,.12)}
.form-title{position:absolute;left:29px;top:32px;color:var(--white);font-size:21px;font-weight:400}
.form-title strong{font-weight:700}
.field,.submit{position:absolute;height:40px;background:var(--white);border:1px solid #ddd;border-radius:2px;font:400 13.5px "Jost",sans-serif;color:var(--field-text);letter-spacing:.6px;padding:0 18px;display:flex;align-items:center;white-space:nowrap}
.field.select{justify-content:space-between}
.submit{background:var(--orange);border:none;color:var(--white);font-weight:700;font-size:16px;letter-spacing:1.2px;justify-content:center}
.portrait{position:absolute;left:575px;top:35px;width:170px;height:535px;border-radius:70px 70px 20px 20px;background:linear-gradient(180deg,#d9c9b8 0%,#8f857c 25%,#7e756d 70%,#3a3a3a 100%)}
.offer{position:absolute;left:791px;top:226px;width:360px}
.offer h2{font-size:29px;font-weight:700;color:var(--ink);margin-bottom:10px}
.offer ul{list-style:none}
.offer li{display:flex;align-items:center;gap:15px;font-size:21px;height:44px;white-space:nowrap}
.tick{width:26px;height:26px;background:var(--orange);display:flex;align-items:center;justify-content:center}
.lead-name{margin-top:12px;font-size:20px;white-space:nowrap}
.signature{position:absolute;left:798px;top:455px;width:266px;height:50px;background:linear-gradient(90deg,rgba(232,87,12,.25),rgba(232,87,12,.1))}
.expert{position:absolute;top:586px;left:0;width:1200px;height:140px;background:var(--sand)}
.expert-name{position:absolute;left:0;top:0;width:466px;height:140px;background:var(--sand-dark);color:var(--white);padding:34px 0 0 113px;white-space:nowrap}
.expert-name h1{font-size:29px;font-weight:700;line-height:1.05;letter-spacing:.5px}
.expert-name p{font-size:28px;line-height:1.2}
.expert-text{position:absolute;left:507px;top:28px;width:600px;color:var(--white);font-size:15px;line-height:30px}
.seo{position:absolute;top:750px;left:112px;width:880px}
.seo h3{color:var(--orange);font-size:14.5px;font-weight:700;letter-spacing:.6px}
.seo p{margin-top:6px;font-size:13.2px;line-height:30px;color:#444}
.site-footer{position:absolute;left:0;top:865px;width:1200px;height:55px;background:var(--footer);color:var(--muted);font-size:13.5px}
.site-footer .copy{position:absolute;left:113px;top:17px}
.site-footer .powered{position:absolute;right:89px;top:16px;font-size:15px}
</style>
</head>
<body>
<header class="site-header">
  <div class="brand">Kernfeld</div>
</header>

<section class="hero">
  <div class="form-card">
    <p class="form-title"><strong>kostenlose</strong> Telefonberatung</p>
    <div class="field" style="left:29px;top:80px;width:183px">Vor- und Nachname</div>
    <div class="field select" style="left:225px;top:80px;width:227px">Geschlecht wählen
      <svg width="10" height="6" viewBox="0 0 10 6"><path d="M1 1l4 4 4-4" fill="none" stroke="#777" stroke-width="1.3"/></svg></div>
    <div class="field" style="left:29px;top:141px;width:227px">E-Mail Adresse</div>
    <div class="field" style="left:269px;top:141px;width:183px">Telefonnummer</div>
    <div class="field" style="left:30px;top:202px;width:182px">Ihre Firma</div>
    <div class="submit" style="left:225px;top:202px;width:228px">JETZT ANMELDEN</div>
  </div>
</section>

<div class="portrait" role="img" aria-label="Foto des Fachbereichsleiters im grauen Anzug, stehend"></div>

<section class="offer">
  <h2>Unser Angebot</h2>
  <ul>
    <li><span class="tick"><svg width="16" height="12" viewBox="0 0 16 12"><path d="M1 6l4 4 10-9" fill="none" stroke="#fff" stroke-width="2"/></svg></span>1 Stunde Erstberatung kostenlos</li>
    <li><span class="tick"><svg width="16" height="12" viewBox="0 0 16 12"><path d="M1 6l4 4 10-9" fill="none" stroke="#fff" stroke-width="2"/></svg></span>Besprechung Ihrer Themen</li>
    <li><span class="tick"><svg width="16" height="12" viewBox="0 0 16 12"><path d="M1 6l4 4 10-9" fill="none" stroke="#fff" stroke-width="2"/></svg></span>Unverbindliche Beratung</li>
  </ul>
  <p class="lead-name">Ihr Fachbereichsleiter Jonas Wendler</p>
</section>
<div class="signature" role="img" aria-label="Handschriftliche Unterschrift von Jonas Wendler"></div>

<section class="expert">
  <div class="expert-name">
    <h1>JONAS WENDLER</h1>
    <p>Ihr Experte für Nexa Security</p>
  </div>
  <p class="expert-text">Ich habe langjährige Erfahrung in Nexa Entwicklungsprojekten und besondere<br>Leidenschaft für Security. Auch die Arbeit mit Nexa-Security kann Spaß machen! Gerne<br>nehme ich mir exklusiv für Sie die Zeit, um über Ihre Themen zu sprechen.</p>
</section>

<section class="seo">
  <h3>SEO TEXT</h3>
  <p>Ich habe langjährige Erfahrung in Nexa Entwicklungsprojekten und besondere Leidenschaft für Security. Auch die Arbeit mit Nexa-Security kann Spaß<br>machen! Gerne nehme ich mir exklusiv für Sie die Zeit, um über Ihre Themen zu sprechen.</p>
</section>

<footer class="site-footer">
  <span class="copy">@ 2015 COPYRIGHT</span>
  <span class="powered">powered by &nbsp;Kernfeld GmbH</span>
</footer>
</body>
</html>
```